VELDA Medical Spa

We'd like a business card with the reverse of the card for appointments. We like round corners and vertical design. We have a background image and bird logo to include with the following wording on the front:-
Velda Medical Spa
58 Brackley Street
NORTH ELMSVALE
SA 5184
Phone 08 83914076
www.veldamedicalspa.com.au
Facebook veldamedicalspa
Instagram veldamedicalspa
On the back I'd like an appointment card layout please.
Cheers Dot

```html
<!DOCTYPE html>
<html lang="en">
<head>
<meta charset="utf-8">
<title>Velda Medical Spa – Business &amp; Appointment Card</title>
<link rel="stylesheet" href="https://fonts.googleapis.com/css2?family=EB+Garamond:ital,wght@0,400;0,500;1,400&display=swap">
<style>
  :root {
    --page-bg: #ececea;
    --mint: #a9dbbe;
    --mint-teal: #8fd2cb;
    --mint-light: #b6e3c6;
    --ink: #1f1f1f;
    --white: #ffffff;
    --dot-line: #8fcfa9;
  }
  * { margin: 0; padding: 0; box-sizing: border-box; }
  html, body {
    width: 1200px; height: 838px; overflow: hidden;
    background: var(--page-bg);
  }
  body {
    position: relative;
    font-family: "EB Garamond", Georgia, serif;
    color: var(--ink);
  }
  .card {
    position: absolute;
    top: 81px;
    width: 390px; height: 673px;
    border-radius: 28px;
    overflow: hidden;
  }
  .card--front { left: 156px; }
  .card--back { left: 645px; background: var(--white); }

  /* Front */
  .front-backdrop {
    position: absolute; inset: 0;
    background: linear-gradient(160deg, var(--mint-light) 0%, var(--mint-teal) 45%, #9ad8c9 70%, var(--mint-light) 100%);
  }
  .logo-frame {
    position: absolute;
    left: 84px; top: 32px;
    width: 223px; height: 254px;
    background: var(--mint);
    border: 2px solid var(--white);
    display: flex; align-items: center; justify-content: center;
  }
  .brand-name {
    color: var(--white);
    font-weight: 500;
    letter-spacing: 0.18em;
    padding-left: 0.18em;
    line-height: 1;
  }
  .logo-frame .brand-name { font-size: 42px; margin-top: 80px; }

  .front-text {
    position: absolute; left: 0; right: 0;
    text-align: center;
    line-height: 1;
    font-weight: 400;
    font-style: normal;
  }
  .business-name { top: 323px; font-size: 36px; }
  .address { top: 358px; font-size: 27px; }
  .address span { display: block; height: 30px; }
  .oldstyle { font-variant-numeric: oldstyle-nums; }

  .contact-list {
    position: absolute; left: 99px; top: 482px;
    list-style: none;
    font-size: 27px; line-height: 1;
  }
  .contact-list li {
    display: flex; align-items: center; gap: 10px;
    height: 30px;
  }
  .contact-icon { width: 18px; height: 18px; flex: none; }
  .website {
    position: absolute; left: 0; right: 0; top: 602px;
    text-align: center; font-size: 27px; line-height: 1;
  }

  /* Back */
  .logo-tile {
    position: absolute; left: 108px; top: 43px;
    width: 160px; height: 188px;
    background: var(--mint);
    display: flex; align-items: center; justify-content: center;
  }
  .logo-tile .brand-name { font-size: 30px; margin-top: 50px; }
  .appointment-title {
    position: absolute; left: 0; right: 0; top: 250px;
    text-align: center;
    font-size: 26px; font-weight: 400;
    letter-spacing: 0.2em; padding-left: 0.2em;
    line-height: 1;
  }
  .form-row {
    position: absolute; left: 33px; right: 39px;
    display: flex; align-items: baseline; gap: 6px;
    font-size: 24px; line-height: 1;
  }
  .form-row .fill {
    flex: 1;
    border-bottom: 2px dotted var(--dot-line);
    height: 1px;
  }
  .row-for { top: 322px; }
  .row-for-extra { top: 372px; left: 36px; }
  .row-date { top: 422px; }
  .row-time { top: 472px; }

  .footer-wave {
    position: absolute; left: 0; bottom: 0;
    width: 390px; height: 160px;
  }
  .cancel-note {
    position: absolute; left: 0; right: 0; top: 573px;
    text-align: center;
    font-style: italic; font-size: 23px; line-height: 28px;
  }
</style>
</head>
<body>

<section class="card card--front" aria-label="Business card front">
  <div class="front-backdrop" role="img" aria-label="Soft mint and teal photograph of palm fronds"></div>

  <div class="logo-frame">
    <span class="brand-name">VELDA</span>
  </div>

  <h1 class="front-text business-name">Velda Medical Spa</h1>
  <address class="front-text address">
    <span class="oldstyle">58 Brackley Street</span>
    <span>NORTH ELMSVALE</span>
    <span class="oldstyle">SA 5184</span>
  </address>

  <ul class="contact-list">
    <li>
      <svg class="contact-icon" viewBox="0 0 18 18" aria-hidden="true">
        <rect x="0" y="0" width="18" height="18" rx="4" fill="#1f1f1f"/>
        <path d="M4 6.5c0-1.5 2.2-2.3 5-2.3s5 .8 5 2.3v1h-2.4v-1.2H6.4v1.2H4z" fill="#fff"/>
        <rect x="5" y="8.5" width="8" height="5.5" rx="1" fill="#fff"/>
      </svg>
      <span class="oldstyle">08 83914076</span>
    </li>
    <li>
      <svg class="contact-icon" viewBox="0 0 18 18" aria-hidden="true">
        <rect x="0" y="0" width="18" height="18" rx="4" fill="#1f1f1f"/>
      </svg>
      <span>veldamedicalspa</span>
    </li>
    <li>
      <svg class="contact-icon" viewBox="0 0 18 18" aria-hidden="true">
        <rect x="1" y="1" width="16" height="16" rx="4" fill="none" stroke="#1f1f1f" stroke-width="2"/>
      </svg>
      <span>veldamedicalspa</span>
    </li>
  </ul>

  <p class="website">www.veldamedicalspa.com.au</p>
</section>

<section class="card card--back" aria-label="Appointment card back">
  <div class="logo-tile">
    <span class="brand-name">VELDA</span>
  </div>

  <h2 class="appointment-title">APPOINTMENT</h2>

  <div class="form-row row-for"><span>For:</span><span class="fill"></span></div>
  <div class="form-row row-for-extra"><span class="fill"></span></div>
  <div class="form-row row-date"><span>Date:</span><span class="fill"></span></div>
  <div class="form-row row-time"><span>Time:</span><span class="fill"></span></div>

  <svg class="footer-wave" viewBox="0 0 390 160" preserveAspectRatio="none" aria-hidden="true">
    <defs>
      <linearGradient id="silverSwoosh" x1="0" y1="0" x2="1" y2="0">
        <stop offset="0" stop-color="#f2f2f2"/>
        <stop offset="0.5" stop-color="#a7a7aa"/>
        <stop offset="1" stop-color="#3a3a3c"/>
      </linearGradient>
    </defs>
    <path d="M0 31 C120 18 200 48 260 58 C320 66 360 48 390 36 L390 160 L0 160 Z" fill="#a9dbbe"/>
    <path d="M0 0 C130 -6 220 28 268 46 C320 62 362 42 390 26 L390 36 C360 48 320 66 260 58 C200 48 120 18 0 31 Z" fill="url(#silverSwoosh)"/>
  </svg>

  <p class="cancel-note">If unable to keep the appointment,<br>please call.</p>
</section>

</body>
</html>
```